Luma Harbor Vow Studio, Inc.

Luma Harbor Vow Studio Business Card design for Cardlyne. Clean, contemporary, creative, colorful (using colors provided). ONE SIDE SHOULD INCLUDE logo, www.lumaharborvowstudio.com, @sayidoatluma. OTHER SIDE SHOULD INCLUDE Delia Brennan. Owner & Officiant. Brisa Point, Coral Isle. 555.014.2871. delia@lumaharborvowstudio.com. Colors are blue #58AA9E
and golden #e2bf80)

Target Market(s)

Destination Wedding Clients in the United States

Contact Information for Business Card

Delia Brennan
Owner & Officiant
Brisa Point, Coral Isle
555.014.2871
delia@lumaharborvowstudio.com

Font styles to use
Sans Serif

Requirements
Must have
• Colorful (colors are blue #58AA9E
• and golden #e2bf80), clean, contemporary. ONE SIDE SHOULD INCLUDE logo, www.lumaharborvowstudio.com, @sayidoatluma. Other side should include Delia Brennan. Owner & Officiant. Brisa Point, Coral Isle. 555.014.2871. delia@lumaharborvowstudio.com
Nice to have
• I would like to see a version that includes my bio photo, and one that doesn't include the bio photo

```html
<!DOCTYPE html>
<html lang="en">
<head>
<meta charset="utf-8">
<title>Luma Harbor Vow Studio – Business Card</title>
<link rel="stylesheet" href="https://fonts.googleapis.com/css2?family=EB+Garamond:wght@400;600&display=swap">
<style>
  :root {
    --sea-teal: #58aa9e;
    --golden: #e2bf80;
    --golden-text: #d9a95a;
    --card-white: #ffffff;
    --ink: #2b2b2b;
    --stage: #3a3a3c;
    --faint-shell: rgba(0, 0, 0, 0.035);
    --faint-shell-on-teal: rgba(255, 255, 255, 0.08);
  }
  * { box-sizing: border-box; margin: 0; padding: 0; }
  html, body {
    width: 1200px; height: 1000px; overflow: hidden;
    background: var(--stage);
    font-family: "EB Garamond", Georgia, serif;
  }
  .canvas { position: relative; width: 1200px; height: 1000px; }

  .card {
    position: absolute;
    width: 640px; height: 366px;
    border-radius: 26px;
    overflow: hidden;
  }

  /* Front side */
  .card--front { left: 280px; top: 80px; background: var(--sea-teal); color: var(--card-white); }
  .front__decor {
    position: absolute; left: -40px; top: -30px; width: 420px; height: 420px;
    border-radius: 50%;
    background: radial-gradient(circle, var(--faint-shell-on-teal) 0%, rgba(255,255,255,0) 70%);
  }
  .front__emblem {
    position: absolute; left: 260px; top: 34px; width: 120px; height: 78px;
    border-radius: 12px;
    background: linear-gradient(135deg, rgba(255,255,255,0.55), rgba(255,255,255,0.25));
  }
  .front__brand {
    position: absolute; left: 0; right: 0; top: 130px;
    text-align: center;
    font-size: 44px; font-weight: 400; letter-spacing: 1px; white-space: nowrap;
  }
  .front__rule {
    position: absolute; left: 150px; right: 150px; top: 208px;
    height: 1.5px; background: var(--card-white);
  }
  .front__links {
    position: absolute; left: 0; right: 0; top: 224px;
    text-align: center; font-size: 19px; line-height: 1.4;
  }
  .front__handle { display: inline-flex; align-items: center; gap: 6px; }
  .front__dot { width: 10px; height: 10px; border-radius: 50%; background: var(--card-white); display: inline-block; }

  /* Back side */
  .card--back { left: 280px; top: 530px; background: var(--card-white); color: var(--ink); }
  .back__decor {
    position: absolute; left: 300px; top: 40px; width: 320px; height: 300px;
    border-radius: 40% 50% 45% 55%;
    background: radial-gradient(circle, var(--faint-shell) 0%, rgba(0,0,0,0) 72%);
  }
  .back__contact {
    position: absolute; left: 36px; top: 250px;
    list-style: none; font-size: 17px; line-height: 1.45;
  }
  .back__contact li { display: flex; align-items: center; gap: 7px; white-space: nowrap; }
  .back__contact svg { width: 13px; height: 13px; flex: none; }
  .back__identity {
    position: absolute; right: 40px; bottom: 34px; text-align: left;
  }
  .back__name { font-size: 26px; font-weight: 600; color: var(--sea-teal); white-space: nowrap; }
  .back__role { font-size: 17px; color: var(--golden-text); margin-left: 22px; white-space: nowrap; }
</style>
</head>
<body>
<main class="canvas">

  <section class="card card--front" aria-label="Card front">
    <div class="front__decor" role="img" aria-label="Faint seashell decoration"></div>
    <div class="front__emblem" role="img" aria-label="Seashell and starfish illustration"></div>
    <h1 class="front__brand">Luma Harbor Vow Studio</h1>
    <div class="front__rule"></div>
    <p class="front__links">
      www.lumaharborvowstudio.com<br>
      <span class="front__handle"><span class="front__dot"></span>@sayidoatluma</span>
    </p>
  </section>

  <section class="card card--back" aria-label="Card back">
    <div class="back__decor" role="img" aria-label="Faint seashell and starfish decoration"></div>
    <ul class="back__contact">
      <li>
        <svg viewBox="0 0 12 12"><path d="M6 0.5a4 4 0 0 0-4 4c0 3 4 7 4 7s4-4 4-7a4 4 0 0 0-4-4z" fill="var(--sea-teal)"/><circle cx="6" cy="4.5" r="1.5" fill="#fff"/></svg>
        Brisa Point, Coral Isle.
      </li>
      <li>
        <svg viewBox="0 0 12 12"><path d="M2.5 1l2 .3.8 2.4-1.2 1a7 7 0 0 0 3.2 3.2l1-1.2 2.4.8.3 2c-.3.6-1 1-1.7 1A9.5 9.5 0 0 1 1 2.7c0-.7.4-1.4 1-1.7z" fill="var(--sea-teal)"/></svg>
        555.014.2871.
      </li>
      <li>
        <svg viewBox="0 0 12 12"><rect x="0.5" y="2" width="11" height="8" rx="2" fill="var(--sea-teal)"/><path d="M1.5 3l4.5 3.5L10.5 3" stroke="#fff" stroke-width="1" fill="none"/></svg>
        delia@lumaharborvowstudio.com
      </li>
    </ul>
    <div class="back__identity">
      <p class="back__name">Delia Brennan</p>
      <p class="back__role">Owner &amp; Officiant</p>
    </div>
  </section>

</main>
</body>
</html>
```